Instagram Advert of Mobile App Launch event

I need an instagram post for a new mobile application for the launching campaign. The mobile application is for booking appointments in salons and with makeup artists (freelancers).

The target audience are the clients where we`ll ask them to tag their friends, download the app and create an account.

A draw will take a place after 1 week, and the winner and the tagged friend will get a Veloranne bracelet.

The post should contain the app logo (attached) and Veloranne logo.

Target Market(s)

Ladies in Kuwait only

Industry/Entity Type

Beauty Salon

Colors
ec1f27
ffc214
e667a6
e34197
a64599
f04a50

Requirements
Must have
• the app logo, Veloranne logo and to be modern style
Nice to have
• salon tools like makeup, hair brush, scissor,...
Should not have
• no human models

```html
<!DOCTYPE html>
<html lang="en">
<head>
<meta charset="utf-8">
<title>belvia – Launch Post</title>
<link rel="stylesheet" href="https://fonts.googleapis.com/css2?family=Quicksand:wght@500;700&family=Open+Sans:wght@400&display=swap">
<style>
  :root {
    --red: #ec1f27;
    --yellow: #ffc214;
    --pink-light: #e667a6;
    --pink: #e34197;
    --purple: #a64599;
    --coral: #f04a50;
    --plum: #9c1f63;
    --grey-text: #6e6e73;
    --logo-grey: #a3a3a6;
    --phone-body: #f4f4f6;
    --phone-edge: #c9c9cd;
    --paper: #ffffff;
  }
  html, body {
    margin: 0;
    padding: 0;
    overflow: hidden;
    background: var(--paper);
  }
  .post {
    position: relative;
    width: 1200px;
    height: 1200px;
    overflow: hidden;
    background: var(--paper);
    font-family: "Quicksand", sans-serif;
  }
  .backdrop {
    position: absolute;
    inset: 0;
    width: 1200px;
    height: 1200px;
  }

  /* brand lock-up, top right */
  .brand {
    position: absolute;
    top: 24px;
    right: 40px;
    display: flex;
    flex-direction: column;
    align-items: center;
    gap: 8px;
  }
  .brand-dot {
    width: 98px;
    height: 98px;
    border-radius: 50%;
    background: var(--pink);
  }
  .brand-name {
    font-weight: 700;
    font-size: 50px;
    line-height: 1;
    color: var(--logo-grey);
    letter-spacing: 1px;
  }

  /* phone */
  .phone {
    position: absolute;
    left: 158px;
    top: 212px;
    width: 378px;
    height: 655px;
    border-radius: 52px;
    background: var(--phone-body);
    border: 3px solid var(--phone-edge);
    box-shadow: 0 14px 30px rgba(0,0,0,0.18);
    transform: rotate(11deg);
    transform-origin: center;
  }
  .phone-speaker {
    position: absolute;
    top: 36px;
    left: 50%;
    width: 52px;
    height: 6px;
    margin-left: -26px;
    border-radius: 3px;
    background: #55555a;
  }
  .phone-camera {
    position: absolute;
    top: 16px;
    left: 50%;
    width: 8px;
    height: 8px;
    margin-left: -4px;
    border-radius: 50%;
    background: #55555a;
  }
  .phone-home {
    position: absolute;
    bottom: 24px;
    left: 50%;
    width: 46px;
    height: 46px;
    margin-left: -26px;
    border-radius: 50%;
    border: 3px solid var(--phone-edge);
  }
  .screen {
    position: absolute;
    top: 72px;
    left: 22px;
    right: 22px;
    height: 488px;
    border: 2px solid #2b2b2e;
    background: linear-gradient(180deg, #f6f3f6 0%, #f1e6ee 45%, #e9cde0 75%, #e6c4dc 100%);
    display: flex;
    flex-direction: column;
    align-items: center;
    text-align: center;
  }
  .screen-brand {
    margin-top: 34px;
    display: flex;
    flex-direction: column;
    align-items: center;
    gap: 6px;
  }
  .screen-brand .brand-dot {
    width: 58px;
    height: 58px;
  }
  .screen-brand .brand-name {
    font-size: 32px;
    color: var(--grey-text);
  }
  .screen-headline {
    margin: 34px 0 6px;
    font-weight: 700;
    font-size: 20px;
    color: var(--pink);
    letter-spacing: 0.3px;
  }
  .screen-tagline {
    margin: 0;
    font-weight: 500;
    font-size: 19px;
    line-height: 1.1;
    color: var(--grey-text);
    text-transform: uppercase;
  }
  .screen-actions {
    margin-top: auto;
    margin-bottom: 34px;
    width: 272px;
    display: flex;
    flex-direction: column;
    gap: 12px;
  }
  .btn {
    height: 40px;
    border-radius: 10px;
    font-family: "Open Sans", sans-serif;
    font-size: 14px;
    display: flex;
    align-items: center;
    justify-content: center;
  }
  .btn-primary {
    background: var(--plum);
    color: #ffffff;
  }
  .btn-secondary {
    background: #ffffff;
    color: #333336;
  }

  .ribbon-label {
    font-family: "Quicksand", sans-serif;
    font-weight: 700;
    font-size: 30px;
    fill: #ffffff;
  }
</style>
</head>
<body>
<main class="post">

  <svg class="backdrop" viewBox="0 0 1200 1200" xmlns="http://www.w3.org/2000/svg">
    <defs>
      <linearGradient id="splashTone" x1="0" y1="0" x2="0.25" y2="1">
        <stop offset="0" stop-color="#ffc214" stop-opacity="0.85"/>
        <stop offset="0.3" stop-color="#f8a450" stop-opacity="0.7"/>
        <stop offset="0.55" stop-color="#f04a50" stop-opacity="0.65"/>
        <stop offset="0.8" stop-color="#e667a6" stop-opacity="0.7"/>
        <stop offset="1" stop-color="#a64599" stop-opacity="0.9"/>
      </linearGradient>
      <linearGradient id="toolsTone" x1="0" y1="0" x2="0" y2="1">
        <stop offset="0" stop-color="#ffc214" stop-opacity="0.55"/>
        <stop offset="0.3" stop-color="#e34197" stop-opacity="0.35"/>
        <stop offset="0.6" stop-color="#a64599" stop-opacity="0.4"/>
        <stop offset="1" stop-color="#6a2a5c" stop-opacity="0.45"/>
      </linearGradient>
    </defs>

    <g class="watercolor-splash" role="img" aria-label="Watercolour splash in yellow, coral, pink and purple">
      <path fill="url(#splashTone)" d="M430,20 C560,0 700,40 760,120 C900,180 870,320 830,420 C910,560 990,700 1030,820 C1110,900 1200,940 1200,1000 L1200,1200 L520,1200 C470,1100 420,1000 470,900 C430,800 480,700 520,620 C450,500 420,400 470,300 C420,200 400,100 430,20 Z"/>
      <circle cx="1015" cy="805" r="11" fill="#ec1f27"/>
      <circle cx="1060" cy="818" r="6" fill="#ec1f27"/>
      <circle cx="1100" cy="822" r="8" fill="#ec1f27"/>
      <circle cx="1160" cy="820" r="12" fill="#ec1f27"/>
      <circle cx="985" cy="790" r="4" fill="#ec1f27"/>
    </g>

    <rect class="beauty-tools" role="img" aria-label="Mascara wands, makeup brushes, lipstick, comb and thinning scissors laid in a diagonal column"
          x="520" y="10" width="260" height="1130" rx="130"
          fill="url(#toolsTone)" transform="rotate(8 650 575)"/>

    <g class="gift-ribbon">
      <path fill="#e3261c" d="M-10,930 L20,905 L210,1040 L180,1070 Z"/>
      <path fill="#e3261c" d="M150,1010 L190,980 L430,1210 L380,1210 Z"/>
      <circle cx="175" cy="1010" r="18" fill="#c51d15"/>
      <text class="ribbon-label" transform="translate(20,940) rotate(36)">Veloranne</text>
      <text class="ribbon-label" transform="translate(215,1050) rotate(43)">Veloranne</text>
    </g>
  </svg>

  <div class="brand">
    <span class="brand-dot"></span>
    <span class="brand-name">belvia</span>
  </div>

  <div class="phone">
    <span class="phone-camera"></span>
    <span class="phone-speaker"></span>
    <section class="screen">
      <div class="screen-brand">
        <span class="brand-dot"></span>
        <span class="brand-name">belvia</span>
      </div>
      <h2 class="screen-headline">FIND AND BOOK</h2>
      <p class="screen-tagline">Hair, make up<br>beauty salons and<br>professionals</p>
      <div class="screen-actions">
        <div class="btn btn-primary">Create New Account</div>
        <div class="btn btn-secondary">Log In</div>
      </div>
    </section>
    <span class="phone-home"></span>
  </div>

</main>
</body>
</html>
```